Redesign of existing website for a corporate advisory business focussed on technology

We need a redesign of our website. We are a corporate advisory business based in Sydney. Our focus is on the technology and life-science sectors. We assist our clients with capital raisings, mergers and acquisitions and other corporate transactions.

Our business is called "Harbourline Capital Advisors"
Our current website is www.harbourlinecap.com.au

I'd like to see a complete re-design of the site. (I'm happy to keep any of the existing images - but equally happy to scrap them completely and "start again".)

My preference is that the logo remain as it is. However, I would be very open to a re-colouring of the logo if it works better with a new webiste design.

The content of the website will remain the same. I'd like one additional section - "News" - which will allow us to manually post news items and which will pull in news feeds from current and past clients.

In terms of positioning / look-and-feel:

Our clients fall into two categories. I'd like the website to appeal to both:

1. The first category is: Executives from established technology or life-science companies (private or public), who engage us to assist with strategy, capital raising, corporate transactions.

2. The second category is: Entrepreneurs looking for advice in accessing angel funding or venture capital. The site should appeal to young tech-savvy entrepreneurs who are looking to engage a firm to provide such assistance.

To accomodate both target groups, the overriding feel should be one of professionalism, stability, trust and expertise. However, while the site should look fairly "corporate", I'd like it to feel contemporary and have an element of creativity and flair, reflecting the fact that our clients are often early-stage, innovative, technology companies. (I know this might be a tricky balance...)

Target Market(s)

Potential clients. Typically executives at technology or life-science companies or (more typically) entrepreneurs building their own companies

Industry/Entity Type

Business

Requirements
Must have
• 1. All content on the existing website
2. An additional section called "News" that allows us to easily add news items or articles and ideally which accepts news feeds from a handful of past and present clients
3. An ability to easily update and edit content
Should not have
• The site should not have "gimmicks". (Definitely no devices like the moving arrow in the current site!)

It should be fairly conservative, while still feeling contemporary and fresh.

```html
<!DOCTYPE html>
<html lang="en">
<head>
<meta charset="utf-8">
<title>Harbourline Capital Advisors</title>
<link href="https://fonts.googleapis.com/css2?family=Arimo:ital,wght@0,400;0,700;1,400;1,700&display=swap" rel="stylesheet">
<style>
:root{
  --orange:#d4743a;
  --orange-deep:#c8602a;
  --band:#d4d4d4;
  --frame:#e6e6e6;
  --text:#444;
  --news-blue:#5a73a6;
  --footer:#2b2b2b;
  --field:#222;
  --footer-text:#cfcfcf;
  --footer-muted:#8a8a8a;
  --button:#3d3d3d;
}
*{margin:0;padding:0;box-sizing:border-box}
html,body{width:1200px;height:1187px;overflow:hidden;background:#fff}
body{position:relative;font-family:"Arimo",Arial,sans-serif;color:var(--text)}
.abs{position:absolute}

.brand{left:116px;top:30px;display:flex;align-items:center;gap:14px}
.brand-mark{width:71px;height:71px;border-radius:50%;background:var(--orange)}
.brand-name{font-size:23px;color:#3a3a3a;font-weight:400}

.search{left:819px;top:24px;width:271px;height:39px;background:#efefef;display:flex;align-items:center;justify-content:space-between;padding:0 12px 0 10px;font-size:12px;color:#888}
.header-rule{left:495px;top:68px;width:597px;height:1px;background:#d9b79c}

.main-nav{left:561px;top:94px;display:flex;gap:0;font-size:17px}
.main-nav a{color:var(--orange);text-decoration:none;padding:6px 10px;height:32px;line-height:20px}
.main-nav a.current{background:var(--orange);color:#fff;width:82px;text-align:center}

.band{left:0;top:360px;width:1200px;height:586px;background:var(--band)}

.slider{left:112px;top:152px;width:975px;height:388px;background:var(--frame)}
.slider-shadow{left:128px;top:538px;width:944px;height:14px;border-radius:50%;background:radial-gradient(ellipse at center,rgba(0,0,0,.35),rgba(0,0,0,0) 70%)}
.hero{left:127px;top:160px;width:878px;height:366px;background:linear-gradient(135deg,#d8d2c8 0%,#c9ccd0 35%,#b9c1c9 55%,#e9e1cf 100%)}
.dots{left:133px;top:504px;display:flex;gap:9px}
.dots span{width:10px;height:10px;border-radius:50%;background:#fff}
.social{left:1020px;top:205px;display:flex;flex-direction:column;gap:27px}
.social span{width:50px;height:50px;border-radius:50%;box-shadow:0 3px 0 #1c2a3a}
.social .s1{background:#35506b}
.social .s2{background:#4a6fb5}
.social .s3{background:#3a8fc4}
.social .s4{background:#3f63b0}

.intro{left:112px;top:575px;width:620px}
.intro h1{font-size:18px;font-style:italic;font-weight:700;color:var(--orange-deep);margin-bottom:34px;letter-spacing:-.2px}
.intro p{font-size:13.4px;line-height:17.5px;margin-bottom:13px;text-align:justify}

.divider{left:781px;top:576px;width:2px;height:334px;background:#9a9a9a}

.news{left:813px;top:575px;width:278px}
.news h2{font-size:18.5px;font-style:italic;font-weight:700;color:var(--news-blue);margin-bottom:14px}
.news-item{height:99px}
.news-item p{font-size:12.2px;line-height:16.6px;font-style:italic;text-align:justify;color:#555;padding-left:2px}
.read-more{display:flex;margin-left:167px;margin-top:0;width:110px;height:23px;border-radius:12px;background:var(--button);color:#fff;font-size:12px;align-items:center;justify-content:center;gap:12px;box-shadow:0 2px 2px rgba(0,0,0,.35)}

.footer{left:0;top:946px;width:1200px;height:241px;background:var(--footer)}
.footer h3{font-size:14px;font-weight:400;color:var(--footer-text)}
.about{left:112px;top:966px;width:311px}
.about .rule{height:1px;background:#555;margin:17px 0 16px;border-bottom:1px solid #1a1a1a}
.about p{font-size:10.6px;line-height:12.6px;font-style:italic;color:var(--footer-muted);margin-bottom:13px}
.contact{left:465px;top:966px;width:279px}
.contact h3{margin-bottom:15px}
.field{background:var(--field);border-radius:4px;color:#fff;font-size:10.6px;padding:10px 13px;margin-bottom:8px;height:31px}
.field.msg{height:88px}
.footer-links{left:794px;top:992px;font-size:10.8px;color:var(--footer-text)}
.footer-links nav{display:flex;gap:12px;margin-bottom:19px}
</style>
</head>
<body>

<header>
  <div class="abs brand">
    <span class="brand-mark"></span>
    <span class="brand-name">Harbourline Capital Advisors</span>
  </div>
  <div class="abs search">
    <span>Search</span>
    <svg width="32" height="26" viewBox="0 0 32 26" aria-hidden="true">
      <circle cx="11" cy="10" r="7" fill="none" stroke="#e08a4e" stroke-width="3"/>
      <line x1="16" y1="15" x2="27" y2="23" stroke="#e08a4e" stroke-width="4" stroke-linecap="round"/>
    </svg>
  </div>
  <div class="abs header-rule"></div>
  <nav class="abs main-nav">
    <a class="current">Home</a>
    <a>Our services</a>
    <a>Our team</a>
    <a>Our experience</a>
    <a>Contact us</a>
  </nav>
</header>

<div class="abs band"></div>

<section>
  <div class="abs slider-shadow"></div>
  <div class="abs slider"></div>
  <div class="abs hero" role="img" aria-label="Close-up photograph of dandelion seeds against a soft warm sky"></div>
  <div class="abs dots"><span></span><span></span><span></span></div>
  <div class="abs social" aria-label="Social links">
    <span class="s1"></span><span class="s2"></span><span class="s3"></span><span class="s4"></span>
  </div>
</section>

<main>
  <article class="abs intro">
    <h1>A corporate advisory firm with a focus on life-science and technology</h1>
    <p>Harbourline Capital Advisors is a specialist corporate advisory and investment firm with a focus on high growth companies in the Australian life-science and technology sectors.</p>
    <p>Our team combines extensive investment banking and funds management experience with sector expertise and longstanding investor relationships.</p>
    <p>Our advisory work incorporates both equity capital markets as well as mergers and acquisitions. Via our alliance with specialist US investment bank Meridale Partners LLC, we are well placed to introduce qualified international partnering opportunities to our domestic clients and to provide seamless cross-border transaction execution capabilities.</p>
    <p>Our objective is to partner with our clients over the long term, providing a skilled outsourced corporate capability to help plan, evaluate and execute significant transactions.</p>
  </article>

  <div class="abs divider"></div>

  <aside class="abs news">
    <h2>Latest News</h2>
    <div class="news-item">
      <p>Lorem ipsum dolor sit amet, consectetur adipisicing elit, sed do eiusmod tempor incididunt ut labore et dolore magna aliqua.</p>
      <a class="read-more">Read more <span>›</span></a>
    </div>
    <div class="news-item">
      <p>Lorem ipsum dolor sit amet, consectetur adipisicing elit, sed do eiusmod tempor incididunt ut labore et dolore magna aliqua.</p>
      <a class="read-more">Read More <span>›</span></a>
    </div>
    <div class="news-item">
      <p>Lorem ipsum dolor sit amet, consectetur adipisicing elit, sed do eiusmod tempor incididunt ut labore et dolore magna aliqua.</p>
      <a class="read-more">Read More <span>›</span></a>
    </div>
  </aside>
</main>

<footer class="abs footer">
</footer>
<div class="abs about">
  <h3 style="font-size:14px;color:var(--footer-text);font-weight:400">More About Us</h3>
  <div class="rule"></div>
  <p>Lorem ipsum dolor sit amet, consectetur adipiscing elit.<br>Vivamus eros arcu, luctus eget auctor nec, lobortis vitae urna. Ut et odio ut orci tincidunt fermentum.<br>Fusce venenatis consequat diam sed sodales.</p>
  <p>Lorem ipsum dolor sit amet, consectetur adipiscing elit.<br>Vivamus eros arcu, luctus eget auctor nec, lobortis vitae urna. Ut et odio ut orci tincidunt fermentum.<br>Fusce venenatis consequat diam sed sodales.</p>
</div>
<div class="abs contact">
  <h3 style="font-size:14px;color:var(--footer-text);font-weight:400;margin-bottom:15px">Contact Us</h3>
  <div class="field">Name:</div>
  <div class="field">Email:</div>
  <div class="field msg">Message:</div>
</div>
<div class="abs footer-links">
  <nav><span>Home</span><span>Our services</span><span>Our team</span><span>Our experience</span><span>Contact us</span></nav>
  <p>© Harbourline Capital Advisors Pty Ltd 2011, AFS License No: 512390</p>
</div>

</body>
</html>
```